New name flyer

We have just changed our business name from kR Property group to Harbour Lantern. We want to distribute a flyer to the local community to inform them of the change. We are a realestate agency which focuses mainly on property management but also sales. We service from Brisbane to the Sunshine coast.

Target Market(s)

Local community

Industry/Entity Type

realestate

Requirements
Must have
• Details of name change
Nice to have
• Servicing area Brisbane and Sunshine Coast, no change in management or services we offer, and will continue pride ourselves on offering a high level of service, with the same team from the Gold to Sunshine Coast.
Should not have
• too much wording.

```html
<!DOCTYPE html>
<html lang="en">
<head>
<meta charset="utf-8">
<title>Harbour Lantern – New Name Flyer</title>
<link href="https://fonts.googleapis.com/css2?family=Barlow+Semi+Condensed:wght@500;700;800&display=swap" rel="stylesheet">
<style>
:root{
  --navy:#0c2d62;
  --navy-deep:#071f47;
  --blue:#0d4ea6;
  --yellow:#ffc20e;
  --paper:#f3f6fa;
  --white:#ffffff;
}
*{margin:0;padding:0;box-sizing:border-box}
html,body{width:848px;height:1200px;overflow:hidden;background:var(--white)}
.flyer{position:relative;width:848px;height:1200px;overflow:hidden;
  background:linear-gradient(180deg,#ffffff 0%,var(--paper) 100%);
  font-family:"Barlow Semi Condensed",Arial,sans-serif;color:var(--navy)}
.hero-photo{position:absolute;left:0;top:0;width:848px;height:560px;
  clip-path:polygon(0 0,100% 0,100% 88%,62% 92%,0 91%);
  background:
    radial-gradient(circle at 540px 235px,rgba(255,236,190,.95) 0,rgba(255,220,160,.5) 40px,rgba(255,220,160,0) 140px),
    linear-gradient(180deg,#dfe6ec 0%,#c6cfd6 38%,#8e8a80 58%,#5b5148 78%,#3b342e 100%)}
.hero-fade{position:absolute;left:0;top:0;width:848px;height:560px;
  background:linear-gradient(90deg,rgba(255,255,255,.97) 0%,rgba(255,255,255,.85) 30%,rgba(255,255,255,.2) 58%,rgba(255,255,255,0) 70%),
             linear-gradient(180deg,rgba(255,255,255,.8) 0%,rgba(255,255,255,0) 25%)}
.shapes{position:absolute;left:0;top:0}
.headline{position:absolute;left:60px;top:54px;text-transform:uppercase;font-weight:800;line-height:1}
.headline span{display:block}
.headline .accent{color:var(--yellow);font-size:50px;letter-spacing:.5px}
.headline .big{color:var(--navy);font-size:74px;margin-top:-2px}
.headline .huge{color:var(--navy);font-size:136px;margin-top:-14px;letter-spacing:-1px}
.headline .from{color:var(--yellow);font-size:44px;margin-top:-6px}
.old-name{position:absolute;left:84px;top:474px;width:240px;text-align:center;
  font-weight:700;font-size:38px;line-height:46px;text-transform:uppercase}
.to-label{position:absolute;left:537px;top:556px;width:80px;text-align:center;
  color:var(--yellow);font-weight:700;font-size:36px}
.new-name{position:absolute;left:400px;top:690px;width:350px;display:flex;align-items:center;gap:14px;justify-content:center}
.new-name .mark{width:26px;height:26px;background:var(--navy)}
.new-name .word{font-weight:800;font-size:50px;line-height:48px;text-transform:uppercase;color:var(--navy)}
.about{position:absolute;left:61px;top:760px;font-weight:700;font-size:31px;line-height:43.5px;text-transform:uppercase}
.footer{position:absolute;left:0;bottom:0;width:848px;height:64px;display:flex;align-items:center;
  padding-left:60px;gap:30px;color:var(--white);font-size:18px;font-weight:500}
.footer .item{display:flex;align-items:center;gap:8px}
.corner-name{position:absolute;left:680px;top:1124px;color:var(--white);font-weight:800;font-size:19px;line-height:20px;text-transform:uppercase}
</style>
</head>
<body>
<main class="flyer">
  <div class="hero-photo" role="img" aria-label="Photo of a modern stone villa with balconies overlooking the sea at sunrise"></div>
  <div class="hero-fade"></div>

  <svg class="shapes" width="848" height="1200" viewBox="0 0 848 1200" aria-hidden="true">
    <defs>
      <linearGradient id="ring" x1="0" y1="0" x2="0.3" y2="1">
        <stop offset="0" stop-color="#0d4ea6"/><stop offset="1" stop-color="#061a3d"/>
      </linearGradient>
      <linearGradient id="disc" x1="0" y1="0" x2="0" y2="1">
        <stop offset="0" stop-color="#ffffff"/><stop offset="1" stop-color="#e6ebf2"/>
      </linearGradient>
      <linearGradient id="arrowFill" x1="0" y1="0" x2="1" y2="1">
        <stop offset="0" stop-color="#ffb000"/><stop offset="1" stop-color="#ffe000"/>
      </linearGradient>
    </defs>
    <!-- old name badge -->
    <circle cx="204" cy="545" r="146" fill="url(#ring)"/>
    <circle cx="204" cy="545" r="121" fill="url(#disc)"/>
    <!-- arrow -->
    <polygon points="330,620 372,600 375,630 420,665 396,597 368,612 344,582" fill="url(#arrowFill)"/>
    <!-- new name badge -->
    <circle cx="577" cy="728" r="259" fill="url(#ring)"/>
    <circle cx="577" cy="728" r="226" fill="#ffffff"/>
    <!-- footer -->
    <path d="M600 1140 C660 1140 680 1064 760 1064 L848 1064 L848 1200 L600 1200 Z" fill="#0d4ea6"/>
    <rect x="0" y="1136" width="848" height="64" fill="#0a2752"/>
    <path d="M640 1136 C690 1136 700 1064 760 1064 L848 1064 L848 1136 Z" fill="#0d4ea6"/>
  </svg>

  <h1 class="headline">
    <span class="accent">We have just</span>
    <span class="big">Changed</span>
    <span class="accent">Our business</span>
    <span class="huge">Name</span>
    <span class="from">From</span>
  </h1>

  <p class="old-name">kR<br>Property<br>Group</p>

  <p class="to-label">TO</p>
  <div class="new-name"><span class="mark"></span><span class="word">Harbour<br>Lantern</span></div>

  <p class="about">We are a<br>realestate<br>agency which<br>focuses mainly on<br>property<br>management but also<br>sales. We service from<br>Brisbane to the Sunshine</p>

  <p class="corner-name">Harbour<br>Lantern</p>

  <footer class="footer">
    <span class="item"><svg width="18" height="18" viewBox="0 0 18 18"><circle cx="9" cy="9" r="8" fill="#fff"/></svg>@companyprofile</span>
    <span class="item"><svg width="16" height="20" viewBox="0 0 16 20"><path d="M8 0a8 8 0 0 1 8 8c0 5-8 12-8 12S0 13 0 8a8 8 0 0 1 8-8z" fill="#fff"/><circle cx="8" cy="8" r="3" fill="#0a2752"/></svg>123 street 100e</span>
    <span class="item"><svg width="18" height="18" viewBox="0 0 24 24"><path d="M6.6 10.8a15 15 0 0 0 6.6 6.6l2.2-2.2a1 1 0 0 1 1-.25 11 11 0 0 0 3.6.6 1 1 0 0 1 1 1V20a1 1 0 0 1-1 1A17 17 0 0 1 3 4a1 1 0 0 1 1-1h3.5a1 1 0 0 1 1 1 11 11 0 0 0 .6 3.6 1 1 0 0 1-.25 1z" fill="#fff"/></svg>+00 123 456 789</span>
  </footer>
</main>
</body>
</html>
```